Management Company Needs Web Banners

We need a new set of pixtrel banners developed. Here is what we would like to have:

1. Connect the branding with tangram images from www.VelmarShifts.com
2. Have a "Call to Action" like a "LET'S TALK" Button

1. 728x90 Investments Need Expert Management.
2. 300x250 Senior Living Turnaround Experts
3. 728x90 KIRV Finds Lost Revenue in Senior Living Investments
4. 600x315 Senior Living Turnaround Experts

Target Market(s)

Private Equity, Health Care REITs, physicians, pharmacist, etc.

Industry/Entity Type

Management Consulting

Requirements
Must have
• A branding connection to https://www.VelmarShifts.com/

```html
<!DOCTYPE html>
<html lang="en">
<head>
<meta charset="utf-8">
<title>KIRV Web Banners</title>
<link href="https://fonts.googleapis.com/css2?family=Jost:wght@300;400;700&family=Arimo&display=swap" rel="stylesheet">
<style>
  :root {
    --canvas: #e6e7e9;
    --white: #ffffff;
    --label: #333333;
    --brand: #4a1a5e;
    --rust-dark: #3a1608;
    --rust: #a8431a;
    --stone: #8a8078;
    --band-grey: #cfcfd1;
    --panel-grey: #bcbcbe;
  }
  * { box-sizing: border-box; margin: 0; padding: 0; }
  html, body { width: 1200px; height: 831px; overflow: hidden; }
  body {
    position: relative;
    background: var(--canvas);
    font-family: "Jost", sans-serif;
    font-weight: 300;
    color: var(--white);
  }
  .size-label {
    position: absolute;
    font-family: "Arimo", sans-serif;
    font-size: 11px;
    color: var(--label);
  }
  .banner {
    position: absolute;
    overflow: hidden;
    background: var(--white);
    box-shadow: 2px 3px 5px rgba(0,0,0,0.25);
  }
  .photo {
    position: absolute;
    background:
      radial-gradient(ellipse at 30% 60%, rgba(150,140,130,0.55), transparent 55%),
      radial-gradient(ellipse at 75% 40%, rgba(130,120,112,0.45), transparent 50%),
      linear-gradient(160deg, var(--rust-dark) 0%, var(--rust) 45%, #7a3214 75%, var(--rust-dark) 100%);
  }
  .banner--wide .photo {
    background:
      linear-gradient(180deg, #050302 0%, rgba(10,5,3,0.85) 18%, rgba(0,0,0,0) 50%),
      radial-gradient(ellipse at 25% 75%, rgba(150,140,130,0.55), transparent 50%),
      radial-gradient(ellipse at 70% 55%, rgba(130,120,112,0.45), transparent 45%),
      linear-gradient(160deg, var(--rust-dark) 0%, var(--rust) 50%, #6e2c12 100%);
  }
  .banner--leader .photo {
    background:
      linear-gradient(90deg, #3a1a0c 0%, #6a3a22 25%, #8c7f76 55%, #a39a92 80%, #8d857e 100%);
  }
  .wave { position: absolute; left: 0; }
  .headline { position: absolute; left: 0; width: 100%; text-align: center; line-height: 1; white-space: nowrap; }
  .cta {
    position: absolute;
    border: 3px solid var(--white);
    display: flex; align-items: center; justify-content: center;
    letter-spacing: 0.5px;
    white-space: nowrap;
  }
  .url { position: absolute; line-height: 1; white-space: nowrap; }
  .wordmark {
    position: absolute;
    display: flex; align-items: center; gap: 10px;
    color: var(--brand);
    font-weight: 700;
    line-height: 1;
  }
  .wordmark__dot { border-radius: 50%; background: var(--brand); }
  .leader-copy { position: absolute; left: 253px; white-space: nowrap; line-height: 1; }
</style>
</head>
<body>

  <!-- 300x250 -->
  <span class="size-label" style="left:54px; top:121px;">300x250</span>
  <div class="banner" style="left:52px; top:142px; width:337px; height:280px;">
    <div class="photo" role="img" aria-label="Close-up of rust-orange tangram pieces on weathered stone" style="left:0; top:0; width:337px; height:230px;"></div>
    <svg class="wave" width="337" height="280" viewBox="0 0 337 280">
      <polygon points="0,210 168,195 337,210 337,225 168,205 0,225" fill="var(--band-grey)"/>
      <polygon points="0,225 168,205 337,225 337,280 0,280" fill="var(--white)"/>
    </svg>
    <div class="headline" style="top:37px; font-size:19px;">SENIOR LIVING TURNAROUND</div>
    <div class="headline" style="top:66px; font-size:26px;">EXPERTS</div>
    <div class="cta" style="left:62px; top:114px; width:204px; height:47px; font-size:21px;">LET’S TALK</div>
    <div class="url" style="left:0; width:100%; text-align:center; top:172px; font-size:15px;">www.velmarshifts.com</div>
    <div class="wordmark" style="left:99px; top:228px; font-size:30px;">
      <span class="wordmark__dot" style="width:36px; height:36px;"></span>KIRV
    </div>
  </div>

  <!-- 600x315 -->
  <span class="size-label" style="left:468px; top:79px;">600x315</span>
  <div class="banner banner--wide" style="left:465px; top:106px; width:672px; height:352px;">
    <div class="photo" role="img" aria-label="Close-up of rust-orange tangram pieces on weathered stone" style="left:0; top:0; width:672px; height:295px;"></div>
    <svg class="wave" width="672" height="352" viewBox="0 0 672 352">
      <polygon points="0,280 336,261 672,280 672,295 336,272 0,295" fill="var(--band-grey)"/>
      <polygon points="0,295 336,272 672,295 672,352 0,352" fill="var(--white)"/>
    </svg>
    <div class="headline" style="top:48px; font-size:29px;">SENIOR LIVING TURNAROUND</div>
    <div class="headline" style="top:86px; font-size:36px;">EXPERTS</div>
    <div class="cta" style="left:234px; top:162px; width:204px; height:47px; font-size:23px;">LET’S TALK</div>
    <div class="url" style="left:0; width:100%; text-align:center; top:220px; font-size:16px;">www.velmarshifts.com</div>
    <div class="wordmark" style="left:255px; top:290px; font-size:36px;">
      <span class="wordmark__dot" style="width:44px; height:44px;"></span>KIRV
    </div>
  </div>

  <!-- 728x90 (investments) -->
  <span class="size-label" style="left:326px; top:482px;">728x90</span>
  <div class="banner banner--leader" style="left:322px; top:500px; width:815px; height:101px;">
    <div class="photo" role="img" aria-label="Rust-orange tangram pieces on weathered stone" style="left:200px; top:0; width:615px; height:101px;"></div>
    <svg class="wave" width="240" height="101" viewBox="0 0 240 101">
      <polygon points="206,0 218,50 206,101 218,101 231,50 218,0" fill="var(--panel-grey)"/>
      <polygon points="0,0 206,0 218,50 206,101 0,101" fill="var(--white)"/>
    </svg>
    <div class="wordmark" style="left:20px; top:32px; font-size:34px;">
      <span class="wordmark__dot" style="width:40px; height:40px;"></span>KIRV
    </div>
    <div class="leader-copy" style="top:17px; font-size:21px;">INVESTMENTS NEED</div>
    <div class="leader-copy" style="top:44px; font-size:29px;">EXPERT MANAGEMENT</div>
    <div class="leader-copy" style="top:77px; font-size:15px;">www.velmarshifts.com</div>
    <div class="cta" style="left:625px; top:25px; width:166px; height:55px; font-size:23px;">LET’S TALK</div>
  </div>

  <!-- 728x90 (lost revenue) -->
  <span class="size-label" style="left:326px; top:617px;">728x90</span>
  <div class="banner banner--leader" style="left:322px; top:637px; width:815px; height:101px;">
    <div class="photo" role="img" aria-label="Rust-orange tangram pieces on weathered stone" style="left:200px; top:0; width:615px; height:101px;"></div>
    <svg class="wave" width="240" height="101" viewBox="0 0 240 101">
      <polygon points="206,0 218,50 206,101 218,101 231,50 218,0" fill="var(--panel-grey)"/>
      <polygon points="0,0 206,0 218,50 206,101 0,101" fill="var(--white)"/>
    </svg>
    <div class="wordmark" style="left:20px; top:32px; font-size:34px;">
      <span class="wordmark__dot" style="width:40px; height:40px;"></span>KIRV
    </div>
    <div class="leader-copy" style="top:16px; font-size:20px;">FINDS LOST REVENUE IN</div>
    <div class="leader-copy" style="top:41px; font-size:27px;">SENIOR LIVING INVESTMENTS</div>
    <div class="leader-copy" style="top:74px; font-size:15px;">www.velmarshifts.com</div>
    <div class="cta" style="left:625px; top:25px; width:166px; height:55px; font-size:23px;">LET’S TALK</div>
  </div>

</body>
</html>
```